Page hosted on godaddy.com, Website domain is valdtke4orun.net

Page should be based on design of my campaign flyer. I will put all text inside pages, they can be layout with top navigation and bottom header that contains contact information. Pages should be white background

I will use html to edit, or I can also get an editor if you specify which one your design is compatible with

Items listed below that are underlined are actual HTML pages
Total number of pages (including BLOG) = 18

Site Structure

HOME
Blog – should be a wordpress blog inside this page
TOLV Board
• Why I am running
• About Me
• How to vote
Automotive
• My Automotive Career
• Automotive for Fun
• Specialty car brokerage
Aviation
• Aviation Experience
• My Favorite Aviation Projects
• Aviation Sales Business
Other Experience
• My Complete Timeline
• Entrepreneurial Activities
• Maplund Vineyard
• Commercial Development
• Home Construction
• Education
Photos
Updates

update, I would ideally like to use wordpress for the site design.

```html
<!DOCTYPE html>
<html lang="en">
<head>
<meta charset="utf-8">
<title>Valdtke for TOLV</title>
<link rel="stylesheet" href="https://fonts.googleapis.com/css2?family=Poppins:wght@300;400;500;600;700&family=Barlow+Condensed:wght@500;600&display=swap">
<style>
:root{
  --navy:#0b2f66;
  --navy-deep:#062251;
  --blue-mid:#1d5296;
  --red:#c11d24;
  --red-footer:#c8242b;
  --ink:#3d3d3d;
  --gray-text:#555;
  --gray-line:#d9d9d9;
  --gray-wedge:#e6e6e6;
  --link:#1f4a8a;
  --white:#fff;
  --grass:#5f8a3a;
  --dark-strip:#3c3c3c;
}
*{box-sizing:border-box;margin:0;padding:0}
html,body{width:1200px;height:4035px;overflow:hidden;background:var(--white)}
body{position:relative;font-family:'Poppins',sans-serif;color:var(--gray-text)}
.abs{position:absolute}
.photo{position:absolute}
svg.shape{position:absolute;left:0;display:block}

/* header */
.nav-bar{top:0;left:0;width:1200px;height:100px}
.brand{position:absolute;left:150px;top:40px;width:230px;text-align:center;font-weight:700;font-size:30px;color:var(--red);letter-spacing:1px}
.brand small{display:block;font-size:16px;color:var(--ink);letter-spacing:3px;font-weight:700}
.main-nav{position:absolute;top:36px;left:515px;display:flex;gap:31px;font-family:'Barlow Condensed',sans-serif;font-weight:500;font-size:15.5px;color:var(--white);letter-spacing:.5px}

/* hero */
.badge{left:160px;top:572px;width:108px;height:108px;border-radius:50%;background:var(--red);border:6px solid var(--white);box-shadow:0 0 0 2px #222}
.hook{left:155px;top:722px;font-weight:600;font-size:21px;line-height:29px;color:var(--ink)}
.hook span{color:var(--red);display:block}

/* intro */
.intro-title{left:155px;top:845px;font-weight:300;font-size:36px;color:var(--ink);line-height:42px}
.intro-title strong{display:block;color:var(--red);font-weight:700;font-size:28px;line-height:34px}
.copy{font-size:12.2px;line-height:20.5px;color:var(--gray-text)}
.copy p{margin-bottom:12px}
.copy b{color:var(--link);font-weight:500}
.intro-col{left:155px;top:934px;width:465px}
.intro-wide{left:155px;top:1213px;width:890px}
.caption{left:662px;top:1166px;font-size:9px;color:#fff;font-weight:600}

/* blue band */
.feature{width:300px;color:var(--white)}
.feature h3{font-size:16px;font-weight:600;letter-spacing:.3px;margin-bottom:6px}
.feature p,.feature li{font-size:12px;line-height:19.5px}
.feature ul{padding-left:15px}
.icon-ring{width:88px;height:88px;border:2px solid var(--white);border-radius:50%;display:flex;align-items:center;justify-content:center}

/* gallery */
.gallery-title{left:155px;top:2252px;font-weight:400;font-size:36px;color:var(--ink)}
.gallery-title strong{color:var(--red);font-weight:700}

/* contact */
.contact-card{left:625px;top:3130px;width:418px;height:388px;background:var(--white)}
.contact-card h2{position:absolute;left:25px;top:25px;font-size:36px;font-weight:400;color:var(--ink)}
.contact-card h2 strong{color:var(--red);font-weight:700}
.contact-card .lead{position:absolute;left:25px;top:78px;width:370px;font-size:11px;line-height:17px}
.field{position:absolute;border:1px solid var(--gray-line);height:36px;font-size:9.5px;color:#999;padding:11px 12px}
.submit{position:absolute;left:27px;top:293px;width:102px;height:30px;background:var(--red);color:#fff;font-size:10px;font-weight:600;text-align:center;line-height:30px}
.card-phone{position:absolute;left:0;top:348px;width:208px;height:40px;background:var(--red);color:#fff;font-size:12px;display:flex;align-items:center;justify-content:center;gap:8px}
.card-mail{position:absolute;left:208px;top:348px;width:210px;height:40px;background:#4a4a4a;color:#fff;font-size:12px;display:flex;align-items:center;justify-content:center;gap:8px}

/* footer */
.footer-brand{left:285px;top:3720px;width:230px;text-align:center;font-weight:700;font-size:32px;color:var(--white);letter-spacing:1px}
.footer-brand small{display:block;font-size:16px;letter-spacing:3px}
.footer h4{font-family:'Barlow Condensed',sans-serif;font-weight:600;font-size:19px;color:#fff;letter-spacing:.5px}
.footer h5{font-family:'Barlow Condensed',sans-serif;font-weight:600;font-size:12.5px;color:#fff;margin-bottom:3px}
.footer li{list-style:none;font-size:10.5px;line-height:16px;color:#fff}
.footer .rule{position:absolute;height:1px;background:rgba(255,255,255,.45)}
.contact-line{display:flex;gap:10px;font-size:10.5px;line-height:16px;color:#fff;margin-bottom:4px}
.social{display:flex;gap:12px}
.social span{width:10px;height:10px;border-radius:50%;background:#fff}
.copyright{left:0;top:4003px;width:1200px;height:32px;background:var(--dark-strip);color:#fff;font-size:10.5px;text-align:center;line-height:32px}
</style>
</head>
<body>

<!-- HERO -->
<div class="photo" role="img" aria-label="Red sports sedan parked on a grassy lawn beside a stone barn" style="left:0;top:0;width:1200px;height:800px;background:linear-gradient(180deg,#7b8f5a 0%,#6c9440 40%,#5a8a2f 100%)"></div>
<div class="photo" role="img" aria-label="Red sedan" style="left:190px;top:140px;width:740px;height:330px;background:radial-gradient(ellipse at 50% 50%,#8e1b22 0%,#5c1217 60%,rgba(60,20,20,0) 75%)"></div>

<svg class="shape" style="top:0" width="1200" height="120" viewBox="0 0 1200 120">
  <polygon points="460,0 1200,0 1200,45 1150,80 440,80" fill="var(--navy)"/>
  <polygon points="70,0 465,0 405,118 130,118" fill="var(--white)"/>
</svg>
<div class="brand">VALDTKE<small>FOR TOLV</small></div>
<nav class="main-nav"><span>HOME</span><span>TOLV BOARD</span><span>AUTOMOTIVE</span><span>AVIATION</span><span>OTHER EXPERIENCE</span><span>GALLERY</span></nav>

<svg class="shape" style="top:520px" width="1200" height="300" viewBox="0 0 1200 300">
  <polygon points="0,70 560,190 1200,20 1200,280 0,280" fill="var(--gray-wedge)"/>
  <polygon points="0,110 520,220 1200,120 1200,300 0,300" fill="var(--white)"/>
</svg>
<div class="photo" role="img" aria-label="Portrait of the candidate in a dark suit and blue tie" style="left:735px;top:410px;width:310px;height:362px;background:linear-gradient(180deg,#c9a890 0%,#b08a70 35%,#1b2030 55%,#0f1420 100%)"></div>
<div class="abs badge"></div>
<div class="abs hook">I NEED 30 SECONDS OF YOUR TIME.<span>I PROMISE IT'S IMPORTANT.</span></div>

<!-- INTRO -->
<h1 class="abs intro-title">NEW CARS ARE NOT DESIGNED WITH<strong>MODIFICATION IN MIND</strong></h1>
<div class="abs copy intro-col">
  <p>You are probably aware that some autonomous vehicle technology is showing up as features in cars today and will be mainstream soon. This Technology is called ADAS, or Advanced Driver Assist Systems. What you may not know is that <b>ADAS systems can malfunction when vehicles are modified.</b></p>
  <p>This affects racing, wheels and tires, body modifications, paint (yes, increasing paint thickness on a bumper can cause these systems to read distances wrong), interior changes, and so much more.</p>
  <p style="margin-top:22px"><b>If we don't get in front ADAS</b> as an aftermarket industry, I vehicle customization will impact driver safety and <b>we can expect government regulation preventing modification and customization.</b></p>
</div>
<div class="photo" role="img" aria-label="Black sedan parked on a gravel drive in front of trees" style="left:650px;top:937px;width:393px;height:256px;background:linear-gradient(180deg,#4f7a3a 0%,#6c9a4a 45%,#9a9a8a 75%,#7a7a70 100%)"></div>
<div class="abs caption">1427RWHP Vantor 8.90 @ 159mph</div>
<div class="abs copy intro-wide">
  <p>I can't stand to the side and watch this happen. I love performance cars, racing, vehicle modification, and customization. I managed Drivetek, am president today of Kestra Systems with nearly 400 employees, have an NDRA license, and live the automotive aftermarket.</p>
  <p>I am running for TOLV director because I can drive change. I have made real change in the repair industry thru right to repair and Automaker relationships, and I have the experience, technical expertise, relationships, leadership, motivation, and drive to push the full force of TOLV towards this problem before it's too late. <b>All I need to get started is your vote</b></p>
</div>

<!-- BLUE BAND -->
<svg class="shape" style="top:1325px" width="1200" height="920" viewBox="0 0 1200 920">
  <defs>
    <radialGradient id="bandGlow" cx="45%" cy="45%" r="65%">
      <stop offset="0" stop-color="var(--blue-mid)"/>
      <stop offset="1" stop-color="var(--navy-deep)"/>
    </radialGradient>
  </defs>
  <polygon points="0,50 940,235 1200,150 1200,860 0,760" fill="url(#bandGlow)"/>
  <polygon points="0,50 940,235 1200,150 1200,0 940,150" fill="var(--gray-wedge)"/>
  <polygon points="0,760 260,680 1200,860 1200,920 0,920" fill="var(--white)"/>
  <polygon points="0,760 260,680 640,750 0,920" fill="var(--gray-wedge)"/>
</svg>

<div class="abs icon-ring" style="left:157px;top:1588px">
  <svg width="46" height="46" viewBox="0 0 46 46" fill="none" stroke="#fff" stroke-width="2"><circle cx="26" cy="20" r="14"/><line x1="16" y1="30" x2="5" y2="41"/><text x="21" y="26" fill="#fff" stroke="none" font-size="16" font-family="Poppins">?</text></svg>
</div>
<div class="abs feature" style="left:284px;top:1602px"><h3>PROBLEM</h3><p>ADAS systems often stop functioning when a vehicle is modified.</p></div>

<div class="abs icon-ring" style="left:612px;top:1588px">
  <svg width="46" height="46" viewBox="0 0 46 46" fill="none" stroke="#fff" stroke-width="2"><circle cx="23" cy="23" r="9"/><line x1="23" y1="4" x2="23" y2="10"/><line x1="23" y1="36" x2="23" y2="42"/><line x1="4" y1="23" x2="10" y2="23"/><line x1="36" y1="23" x2="42" y2="23"/></svg>
</div>
<div class="abs feature" style="left:741px;top:1584px"><h3>SOLUTION</h3><p>My Solution is to activate the full strength of TOLV and it's network to engage Automakers, Members, Regulators, and Industry. Vehicles must be designed with modification in mind, and there must be a partnership and transparency with the aftermarket.</p></div>

<div class="abs icon-ring" style="left:157px;top:1787px">
  <svg width="46" height="46" viewBox="0 0 46 46" fill="none" stroke="#fff" stroke-width="2"><rect x="14" y="6" width="24" height="20" transform="rotate(-20 26 16)"/><path d="M6 40 L18 26 L28 32"/></svg>
</div>
<div class="abs feature" style="left:284px;top:1782px"><h3>LEADERSHIP</h3><p>I bring my Leadership and Experience as President of Kestra Systems, a technology business that helps technicians with complex vehicles repairs and ADAS calibration, previous General Manager of Drivetek, experience and involvement with right to repair regulations, Automaker and government relationships, and inventor on over 60 patents.</p></div>

<div class="abs icon-ring" style="left:612px;top:1787px">
  <svg width="46" height="46" viewBox="0 0 46 46" fill="none" stroke="#fff" stroke-width="2"><circle cx="23" cy="23" r="17"/><circle cx="23" cy="23" r="10"/><circle cx="23" cy="23" r="3"/><line x1="23" y1="23" x2="40" y2="6"/></svg>
</div>
<div class="abs feature" style="left:741px;top:1782px;width:310px"><h3>MY PASSIONS KEEP ME MOTIVATED</h3>
  <ul><li>Resto-mod projects at home (last was a 75 Trailmark powertrain swap)</li><li>Fast Cars (Several 1000+ HP)</li><li>NDRA Comp Licensed Driver</li><li>Pilot, multi engine, instrument and Jet rated</li><li>Hobbyist collector car broker</li><li>Hobbyist airplane dealer</li><li>Driving change in whatever I do</li></ul>
</div>

<!-- GALLERY -->
<h2 class="abs gallery-title">PHOTO <strong>GALLERY</strong></h2>
<div class="photo" role="img" aria-label="Small jet parked on an airport ramp under blue sky" style="left:157px;top:2330px;width:285px;height:220px;background:linear-gradient(180deg,#2f6fc0 0%,#6aa0d8 60%,#8b8b8b 100%)"></div>
<div class="photo" role="img" aria-label="Pilot and child inside an aircraft cockpit" style="left:459px;top:2330px;width:286px;height:220px;background:linear-gradient(135deg,#d8d8d8 0%,#7a7a7a 55%,#3a3a3a 100%)"></div>
<div class="photo" role="img" aria-label="Twin engine airplane flying over farmland" style="left:760px;top:2330px;width:283px;height:220px;background:linear-gradient(180deg,#9aa4ad 0%,#7d8a84 55%,#5d6d52 100%)"></div>
<div class="photo" role="img" aria-label="Engine block with pistons on a workbench" style="left:157px;top:2566px;width:285px;height:214px;background:linear-gradient(135deg,#b9b5ae 0%,#7c7367 60%,#a87a4d 100%)"></div>
<div class="photo" role="img" aria-label="Drag strip with a race car at the starting line" style="left:459px;top:2566px;width:286px;height:214px;background:linear-gradient(180deg,#b8cde6 0%,#8fa0b0 45%,#4a4a4a 100%)"></div>
<div class="photo" role="img" aria-label="Supercharged V8 engine bay of a sedan" style="left:760px;top:2566px;width:283px;height:214px;background:linear-gradient(135deg,#6a6a6a 0%,#2b2b2b 55%,#4a4a4a 100%)"></div>

<!-- CONTACT -->
<div class="photo" role="img" aria-label="Black sedan parked on gravel in front of trees and a lawn" style="left:0;top:2920px;width:1200px;height:720px;background:linear-gradient(180deg,#3f6b2e 0%,#5c8a3a 45%,#8b8b7a 75%,#6f6f66 100%)"></div>
<svg class="shape" style="top:2880px" width="1200" height="110" viewBox="0 0 1200 110">
  <polygon points="0,0 1200,0 1200,40 940,110 0,60" fill="var(--white)"/>
  <polygon points="820,0 1200,0 1200,40 940,110" fill="var(--gray-wedge)"/>
</svg>
<svg class="shape" style="top:3500px" width="1200" height="140" viewBox="0 0 1200 140">
  <polygon points="0,80 360,140 0,140" fill="var(--gray-wedge)"/>
  <polygon points="0,130 280,60 1200,100 1200,140 0,140" fill="var(--white)"/>
</svg>

<div class="abs contact-card">
  <h2>CONTACT <strong>US</strong></h2>
  <p class="lead">Learn more details on the challenge, my vision for solving these problems, and my credentials and experience to make it happen.</p>
  <div class="field" style="left:27px;top:122px;width:176px">First Name</div>
  <div class="field" style="left:210px;top:122px;width:180px">Last Name</div>
  <div class="field" style="left:27px;top:172px;width:176px">Email</div>
  <div class="field" style="left:210px;top:172px;width:180px">Phone</div>
  <div class="field" style="left:27px;top:221px;width:363px;height:64px">Type Your Message Here</div>
  <div class="submit">SUBMIT</div>
  <div class="card-phone"><svg width="12" height="12" viewBox="0 0 24 24" fill="#fff"><path d="M6 2l4 5-2 3c1 3 3 5 6 6l3-2 5 4-3 4C10 22 2 14 2 5z"/></svg>1200-4400-5678</div>
  <div class="card-mail"><svg width="13" height="10" viewBox="0 0 26 20" fill="none" stroke="#fff" stroke-width="2"><rect x="1" y="1" width="24" height="18"/><path d="M1 1l12 10 12-10"/></svg>info@valdtke4orun.net</div>
</div>

<!-- FOOTER -->
<svg class="shape" style="top:3610px" width="1200" height="400" viewBox="0 0 1200 400">
  <polygon points="0,140 360,35 1200,100 1200,400 0,400" fill="var(--red-footer)"/>
</svg>
<div class="abs footer-brand">VALDTKE<small>FOR TOLV</small></div>

<footer class="footer">
  <h4 class="abs" style="left:155px;top:3803px">NAVIGATION</h4>
  <div class="rule" style="left:155px;top:3830px;width:690px"></div>
  <div class="abs" style="left:155px;top:3840px"><h5>TOLV BOARD</h5><ul><li>Why I am running</li><li>About Me</li><li>How to vote</li></ul></div>
  <div class="abs" style="left:155px;top:3922px"><h5>AUTOMOTIVE</h5><ul><li>My Automotive Career</li><li>Automotive for Fun</li><li>Specialty car brokerage</li></ul></div>
  <div class="abs" style="left:385px;top:3840px"><h5>AVIATION</h5><ul><li>Aviation Experience</li><li>My Favorite Aviation Projects</li><li>Aviation Sales Business</li></ul></div>
  <div class="abs" style="left:385px;top:3922px"><h5>AVIATION</h5><ul><li>Aviation Experience</li><li>My Favorite Aviation Projects</li><li>Aviation Sales Business</li></ul></div>
  <div class="abs" style="left:634px;top:3840px"><h5>OTHER EXPERIENCE</h5><ul><li>My Complete Timeline</li><li>Entrepreneurial Activities</li><li>Maplund Vineyard</li><li>Commercial Development</li><li>Home Construction</li><li>Education</li></ul></div>

  <h4 class="abs" style="left:868px;top:3803px">CONTACT US</h4>
  <div class="rule" style="left:868px;top:3830px;width:168px"></div>
  <div class="abs" style="left:868px;top:3840px;width:190px">
    <div class="contact-line"><svg width="10" height="10" viewBox="0 0 24 24" fill="#fff"><path d="M6 2l4 5-2 3c1 3 3 5 6 6l3-2 5 4-3 4C10 22 2 14 2 5z"/></svg>+61 3100 4400</div>
    <div class="contact-line"><svg width="11" height="9" viewBox="0 0 26 20" fill="#fff"><rect x="1" y="1" width="24" height="18"/></svg>support@valdtke4orun.net</div>
    <div class="contact-line"><svg width="10" height="13" viewBox="0 0 20 26" fill="#fff"><path d="M10 0a9 9 0 0 1 9 9c0 7-9 17-9 17S1 16 1 9a9 9 0 0 1 9-9z"/><circle cx="10" cy="9" r="3" fill="var(--red-footer)"/></svg>13/2 Harrow Lane, Eastvale<br>VIC 3999, Australia</div>
    <div class="social" style="margin-top:12px"><span></span><span></span><span></span></div>
  </div>
</footer>
<div class="abs copyright">Copyright © 2022 Brightmoor LLC. All Rights Reserved</div>

</body>
</html>
```